Custom Flooring Website For Tulsa Oklahoma Flooring Store

We need to a design for a website that is in between these two current designs, with a modern look and feel.

https://www.talvenfloors.com/
https://mirelopaving.ca/
We need a home page and 2 interior page styles designed.

Talven Flooring is a locally owned flooring company based in Tulsa, Oklahoma. The website should reflect a professional, established business that sells high-quality flooring products, provides expert installation, and specializes in hardwood floor refinishing. The goal of the site is to clearly communicate trust, craftsmanship, and ease of doing business, while guiding users toward visiting the showroom or requesting service.

The company operates a physical showroom in Tulsa where customers can browse flooring materials in person. Talven Flooring sells five primary product categories: solid hardwood, engineered hardwood, laminate, luxury vinyl plank (LVP), and tile. Tile includes both wall and floor applications, as well as decorative options such as glass tile, metal tile, and natural stone. In addition to product sales, the company offers professional flooring installation, hardwood floor refinishing, and water damage restoration related to flooring.

The website structure is intentionally segmented into three main areas: product pages, service pages, and informational pages (About, Financing, Homepage). Product pages focus on education and selection, helping users understand differences between materials and where they work best. Service pages use a more process-driven layout that explains what to expect before, during, and after work is performed. The homepage serves as an overview, positioning Talven Flooring as a full-service flooring store, tile store, and contractor serving Tulsa and surrounding areas.

Visually, the site should feel clean, approachable, and confidence-inspiring—never flashy or overly sales-driven. The design should support browsing materials, understanding services, and contacting the company easily. Strong emphasis should be placed on clear navigation, readable typography, and a layout that works equally well on desktop and mobile devices.

Calls to action should focus on visiting the showroom, scheduling consultations, and exploring flooring options. The financing page should feel simple and reassuring, reducing friction for users considering larger projects. Overall, the design should reflect a business that values craftsmanship, transparency, and long-term relationships with its customers.

Target Market(s)

Retail Flooring Customers who purchase Hardwood, Engineered, Laminate, Vinyl & Tile. Not carpet

Industry/Entity Type

Flooring Store

Number of Pages Required

3 page

Font styles to use
Sans Serif

Colors

Designer to choose colors to be used in the design.

Requirements
Must have
• We like these two designs (Home Pages) https://www.talvenfloors.com/ https://mirelopaving.ca/
Nice to have
• We need a home page and two interior pages. The website will have 20+ pages coded by our developer, but we will use one home page design and 2 alternating interior pages to fill the website.

```html
<!DOCTYPE html>
<html lang="en">
<head>
<meta charset="utf-8">
<title>Talven Flooring | Tulsa Flooring Store</title>
<link href="https://fonts.googleapis.com/css2?family=Oswald:wght@500&family=Poppins:wght@400;500;600;700&display=swap" rel="stylesheet">
<style>
:root{
  --red:#d0021b;
  --ink:#111;
  --text:#2a2a2a;
  --black:#050505;
  --gray-band:#ebebed;
  --gray-shape:#e6e6e9;
  --pink:#f6dde1;
  --map-fill:#f1f1f3;
  --white:#fff;
  --footer-link:#8a8a8a;
  --footer-rule:#333;
  --accent:#e07b1c;
}
*{box-sizing:border-box;margin:0;padding:0}
html,body{width:1200px;height:4396px;overflow:hidden}
body{position:relative;font-family:"Poppins",sans-serif;color:var(--text);background:var(--white)}
.abs{position:absolute}
.headline{font-family:"Oswald",sans-serif;font-weight:500;color:var(--ink);text-transform:uppercase;letter-spacing:.2px}
.headline em{font-style:normal;color:var(--red)}
.copy{font-size:15.5px;line-height:22.5px}
.copy p+p{margin-top:22px}
.subhead{font-weight:700;color:var(--red);font-size:23px}
.bullets{list-style:none;font-size:16.5px;font-weight:500;color:var(--ink)}
.bullets li{position:relative;padding-left:24px;height:32.5px;line-height:32.5px;white-space:nowrap}
.bullets li::before{content:"";position:absolute;left:2px;top:12px;width:8px;height:8px;background:var(--red);transform:rotate(45deg)}

.site-header{left:0;top:0;width:1200px;height:140px;background:var(--black)}
.brand{display:flex;align-items:center;gap:10px;color:var(--white);font-weight:700;letter-spacing:-.5px;white-space:nowrap}
.brand-mark{width:20px;height:20px;background:var(--accent)}
.header-brand{left:97px;top:44px;font-size:28px}
.contact-line{display:flex;align-items:center;gap:8px;color:var(--white);font-weight:600;font-size:16px;white-space:nowrap}
.main-nav{left:370px;top:82px}
.main-nav a{color:var(--white);text-decoration:none;font-weight:600;font-size:15px;position:absolute;white-space:nowrap}

.hero{left:0;top:140px;width:1200px;height:660px}
.hero-title{left:120px;top:160px;font-size:40px;line-height:47px}
.rule{left:120px;top:336px;width:87px;height:4px;background:var(--red)}
.hero-copy{left:120px;top:363px;width:500px}

.products{left:0;top:800px;width:1200px;height:893px}
.center{width:1200px;text-align:center}
.products-title{top:52px;font-size:40px}
.products-intro{top:114px;width:650px;left:275px;text-align:center}
.products-sub{top:202px}
.products-note{top:797px;width:650px;left:275px;text-align:center}

.services{left:0;top:1693px;width:1200px;height:608px;background:var(--gray-band)}
.services-title{left:582px;top:82px;font-size:40px;line-height:47px}
.services-copy{left:582px;top:190px;width:480px}
.services-sub{left:582px;top:283px}
.services-list{left:582px;top:338px}
.services-close{left:582px;top:459px;width:480px}

.story{left:0;top:2301px;width:1200px;height:729px}
.story-title{left:120px;top:178px;font-size:40px}
.story-copy{left:120px;top:244px;width:535px}
.story-sub{left:120px;top:350px}
.story-list{left:120px;top:406px}
.story-close{left:120px;top:553px;width:490px}

.showroom{left:0;top:3030px;width:1200px;height:632px}
.showroom-title{left:541px;top:232px;font-size:40px;color:var(--white)}
.showroom-copy{left:541px;top:299px;width:510px;color:var(--white)}
.showroom-copy strong{font-weight:700;font-style:italic}

.areas{left:0;top:3662px;width:1200px;height:443px}
.areas-title{left:120px;top:104px;font-size:40px;line-height:47px}
.areas-copy{left:120px;top:216px;width:390px}
.areas-map{left:570px;top:118px;width:420px;height:215px;background:var(--map-fill)}

.site-footer{left:0;top:4105px;width:1200px;height:291px;background:var(--black)}
.footer-brand{left:228px;top:52px;font-size:24px}
.footer-rule{left:150px;top:125px;width:900px;height:1px;background:var(--footer-rule)}
.footer-nav a{position:absolute;top:158px;color:var(--footer-link);text-decoration:none;font-weight:600;font-size:15px;white-space:nowrap}
.copyright{top:202px;font-size:15px;color:var(--white)}
</style>
</head>
<body>

<header class="site-header abs">
  <div class="brand header-brand abs"><span>Talven Flooring</span><span class="brand-mark"></span></div>
  <div class="contact-line abs" style="left:628px;top:26px">
    <svg width="18" height="18" viewBox="0 0 24 24"><path fill="#d0021b" d="M6.6 10.8a15 15 0 0 0 6.6 6.6l2.2-2.2c.3-.3.7-.4 1-.2 1.1.4 2.3.6 3.6.6.6 0 1 .4 1 1V20c0 .6-.4 1-1 1A17 17 0 0 1 3 4c0-.6.4-1 1-1h3.5c.6 0 1 .4 1 1 0 1.3.2 2.5.6 3.6.1.3 0 .7-.2 1z"/></svg>
    (918) 555-0147
  </div>
  <div class="contact-line abs" style="left:808px;top:26px">
    <svg width="18" height="20" viewBox="0 0 24 24"><path fill="none" stroke="#d0021b" stroke-width="2.4" d="M12 22s7-7 7-12a7 7 0 0 0-14 0c0 5 7 12 7 12z"/><circle cx="12" cy="10" r="2.5" fill="#d0021b"/></svg>
    4120 S Harlan Ave, Tulsa, OK 74135
  </div>
  <nav class="main-nav abs">
    <a style="left:0">PRODUCTS</a>
    <a style="left:115px">SERVICES</a>
    <a style="left:215px">REVIEWS</a>
    <a style="left:313px">FINANCING</a>
    <a style="left:429px">INSPIRATION</a>
    <a style="left:553px">ABOUT US</a>
    <a style="left:661px">CONTACT</a>
  </nav>
</header>

<section class="hero abs">
  <svg class="abs" style="left:0;top:0" width="1200" height="660" aria-hidden="true">
    <polygon points="423,0 1200,0 1200,300 870,628" fill="var(--gray-shape)"/>
    <polygon points="990,534 1200,324 1200,760" fill="var(--pink)"/>
  </svg>
  <svg class="abs" style="left:584px;top:17px" width="590" height="590" role="img" aria-label="Photo of a curved modern interior with warm lighting and polished hardwood floor">
    <defs><linearGradient id="g-hero" x1="0" y1="0" x2="0" y2="1"><stop offset="0" stop-color="#8a8378"/><stop offset=".45" stop-color="#a86a2e"/><stop offset="1" stop-color="#6b3512"/></linearGradient></defs>
    <polygon points="295,0 590,295 295,590 0,295" fill="url(#g-hero)"/>
  </svg>
  <h1 class="headline hero-title abs">Tulsa’s local flooring<br>store for <em>quality materials</em><br>&amp; expert installation</h1>
  <div class="rule abs"></div>
  <div class="copy hero-copy abs">
    <p>Talven Flooring is a locally owned flooring store in Tulsa offering quality flooring products, professional installation, and hardwood floor refinishing—all from one trusted team. From our Tulsa showroom, we help homeowners and contractors choose flooring that fits their space, lifestyle, and budget, then install it with care and precision.</p>
    <p>Whether you’re building, remodeling, or restoring existing floors, we provide straightforward guidance, skilled workmanship, and results that last.</p>
  </div>
</section>

<section class="products abs">
  <h2 class="headline products-title center abs"><em>Flooring products</em> for every space</h2>
  <p class="copy products-intro abs">Our showroom features a carefully selected range of flooring options designed to perform well in Tulsa homes and businesses. We carry flooring for both walls and floors, with styles ranging from classic to modern.</p>
  <p class="subhead products-sub center abs">Our flooring selection includes:</p>
  <svg class="abs" style="left:0;top:0" width="1200" height="893">
    <defs>
      <linearGradient id="g-p1" x1="0" y1="0" x2="1" y2="1"><stop offset="0" stop-color="#6e4325"/><stop offset="1" stop-color="#3a2212"/></linearGradient>
      <linearGradient id="g-p2" x1="0" y1="0" x2="0" y2="1"><stop offset="0" stop-color="#b9b4ad"/><stop offset="1" stop-color="#8a6544"/></linearGradient>
      <linearGradient id="g-p3" x1="0" y1="0" x2="0" y2="1"><stop offset="0" stop-color="#8e8f82"/><stop offset="1" stop-color="#7a5538"/></linearGradient>
      <linearGradient id="g-p4" x1="0" y1="0" x2="1" y2="1"><stop offset="0" stop-color="#3a2f25"/><stop offset="1" stop-color="#7a5d42"/></linearGradient>
      <linearGradient id="g-p5" x1="0" y1="0" x2="1" y2="1"><stop offset="0" stop-color="#4a3a2c"/><stop offset="1" stop-color="#9c8f82"/></linearGradient>
    </defs>
    <g font-family="Poppins, sans-serif" font-weight="500" font-size="17" fill="#fff" text-anchor="middle">
      <g role="img" aria-label="Photo of rustic solid hardwood planks">
        <polygon points="273,264 426,417 273,570 120,417" fill="url(#g-p1)"/>
        <text x="273" y="410">Solid hardwood</text><text x="273" y="432">flooring</text>
      </g>
      <g role="img" aria-label="Photo of a living room with engineered hardwood flooring">
        <polygon points="601,264 754,417 601,570 448,417" fill="url(#g-p2)"/>
        <text x="601" y="410">Engineered</text><text x="601" y="432">hardwood flooring</text>
      </g>
      <g role="img" aria-label="Photo of a bright room with laminate flooring">
        <polygon points="925,264 1078,417 925,570 772,417" fill="url(#g-p3)"/>
        <text x="925" y="410">Laminate</text><text x="925" y="432">flooring</text>
      </g>
      <g role="img" aria-label="Photo of luxury vinyl plank flooring">
        <polygon points="437,450 590,603 437,756 284,603" fill="url(#g-p4)"/>
        <text x="437" y="596">Luxury vinyl</text><text x="437" y="618">plank (LVP)</text>
      </g>
      <g role="img" aria-label="Photo of stone tile walls and floor">
        <polygon points="763,450 916,603 763,756 610,603" fill="url(#g-p5)"/>
        <text x="763" y="585">Tile for floors,</text><text x="763" y="607">walls, showers, and</text><text x="763" y="629">backsplashes</text>
      </g>
    </g>
  </svg>
  <p class="copy products-note abs">As a full-service flooring store, we make it easy to compare materials, finishes, and styles in person before making a decision.</p>
</section>

<section class="services abs">
  <svg class="abs" style="left:0;top:0" width="560" height="608" aria-hidden="true">
    <polygon points="210,0 560,0 560,120 300,370" fill="#e2e2e5"/>
  </svg>
  <h2 class="headline services-title abs">Professional installation &amp;<br><em>refinishing services</em></h2>
  <p class="copy services-copy abs">In addition to selling flooring, Talven Flooring provides expert installation and refinishing services. Our experienced team handles projects of all sizes with attention to detail and clear communication from start to finish.</p>
  <p class="subhead services-sub abs">Our services include:</p>
  <ul class="bullets services-list abs">
    <li>Flooring installation for all material types</li>
    <li>Hardwood floor refinishing</li>
    <li>Water damage restoration related to flooring</li>
  </ul>
  <p class="copy services-close abs">By working with one company for both materials and labor, you avoid delays, miscommunication, and unnecessary complications.</p>
</section>

<section class="story abs">
  <h2 class="headline story-title abs">More than a <em>flooring store</em></h2>
  <div class="copy story-copy abs"><p>What sets Talven Flooring apart is experience and craftsmanship. We work closely with homeowners and contractors to ensure every project is done correctly, from subfloor preparation to final trim details.</p></div>
  <p class="subhead story-sub abs">Customers choose us because we offer:</p>
  <ul class="bullets story-list abs">
    <li>A local Tulsa showroom</li>
    <li>Skilled installers and finishers</li>
    <li>Honest recommendations, not pressure</li>
    <li>Quality products selected for long-term performance</li>
  </ul>
  <p class="copy story-close abs">Whether you’re visiting us as a flooring store or a tile store, our focus is on helping you make informed decisions that add lasting value to your space.</p>
</section>

<section class="showroom abs">
  <svg class="abs" style="left:0;top:0" width="1200" height="632" role="img" aria-label="Photo of the Tulsa skyline at dusk blending into red">
    <defs>
      <linearGradient id="g-sky" x1="0" y1="0" x2="1" y2="0"><stop offset="0" stop-color="#2d3550"/><stop offset=".3" stop-color="#5a4a5c"/><stop offset=".5" stop-color="#b0283a"/><stop offset=".75" stop-color="#d0021b"/><stop offset="1" stop-color="#c4001a"/></linearGradient>
      <linearGradient id="g-ground" x1="0" y1="0" x2="0" y2="1"><stop offset="0" stop-color="#000" stop-opacity="0"/><stop offset="1" stop-color="#1d2a1a" stop-opacity=".55"/></linearGradient>
    </defs>
    <rect width="1200" height="632" fill="url(#g-sky)"/>
    <rect width="620" height="632" fill="url(#g-ground)"/>
  </svg>
  <svg class="abs" style="left:194px;top:240px" width="220" height="220" aria-hidden="true">
    <polygon points="110,2 218,110 110,218 2,110" fill="none" stroke="#d9d9d9" stroke-width="8"/>
    <polygon points="110,18 202,110 110,202 18,110" fill="#5a5a66" fill-opacity=".55"/>
    <path d="M110 154s-32-34-32-58a32 32 0 0 1 64 0c0 24-32 58-32 58z" fill="none" stroke="#d0021b" stroke-width="7"/>
    <path d="M96 104v-12l14-12 14 12v12z" fill="#d0021b"/>
  </svg>
  <h2 class="headline showroom-title abs">Visit our Tulsa showroom</h2>
  <div class="copy showroom-copy abs">
    <p>Choosing flooring online only goes so far. Seeing materials in person makes a real difference. We invite you to visit the <strong>Talven Flooring showroom in Tulsa,</strong> where you can explore hardwood, LVP, laminate, and tile options—including wall tile and floor tile—side by side.</p>
    <p>Our team is happy to answer questions, explain differences between materials, and help you plan your next project.</p>
  </div>
</section>

<svg class="abs" style="left:648px;top:2376px" width="552" height="850" role="img" aria-label="Photo of a sunlit living room with a sectional sofa and light hardwood floor">
  <defs><linearGradient id="g-story" x1="0" y1="0" x2="0" y2="1"><stop offset="0" stop-color="#c9a57d"/><stop offset=".5" stop-color="#cfc6b6"/><stop offset="1" stop-color="#a37c57"/></linearGradient></defs>
  <polygon points="415,0 830,425 415,850 0,425" fill="#fff"/>
  <polygon points="415,12 818,425 415,838 12,425" fill="url(#g-story)"/>
</svg>

<svg class="abs" style="left:0;top:1707px" width="500" height="706" role="img" aria-label="Photo of an empty white kitchen with wood floors">
  <defs><linearGradient id="g-kitchen" x1="0" y1="0" x2="0" y2="1"><stop offset="0" stop-color="#d7d7d4"/><stop offset=".5" stop-color="#b3aaa0"/><stop offset="1" stop-color="#8a6d50"/></linearGradient></defs>
  <polygon points="184,0 490,350 184,704 0,496 0,208" fill="#fff"/>
  <polygon points="184,12 478,350 184,692 0,480 0,224" fill="url(#g-kitchen)"/>
</svg>

<section class="areas abs">
  <svg class="abs" style="left:0;top:0" width="1200" height="443" aria-hidden="true">
    <polygon points="1200,20 1070,150 1200,280" fill="var(--pink)"/>
    <polygon points="1200,250 1012,443 1200,443" fill="var(--pink)"/>
  </svg>
  <h2 class="headline areas-title abs">Serving <em>Tulsa</em> &amp;<br>surrounding areas</h2>
  <p class="copy areas-copy abs">Talven Flooring proudly serves Tulsa and nearby communities with reliable flooring products and professional service. Whether you’re updating a single room or planning a full renovation, we’re here to help from start to finish.</p>
  <div class="areas-map abs" role="img" aria-label="County map of Oklahoma with the Tulsa area highlighted"></div>
</section>

<footer class="site-footer abs">
  <div class="brand footer-brand abs"><span>Talven Flooring</span><span class="brand-mark"></span></div>
  <div class="contact-line abs" style="left:500px;top:62px;font-size:15px">
    <svg width="22" height="24" viewBox="0 0 24 24"><path fill="none" stroke="#d0021b" stroke-width="2.2" d="M12 22s7-7 7-12a7 7 0 0 0-14 0c0 5 7 12 7 12z"/><circle cx="12" cy="10" r="2.5" fill="#d0021b"/></svg>
    4120 S Harlan Ave, Tulsa, OK
  </div>
  <div class="contact-line abs" style="left:792px;top:62px;font-size:15px">
    <svg width="18" height="18" viewBox="0 0 24 24"><path fill="#d0021b" d="M6.6 10.8a15 15 0 0 0 6.6 6.6l2.2-2.2c.3-.3.7-.4 1-.2 1.1.4 2.3.6 3.6.6.6 0 1 .4 1 1V20c0 .6-.4 1-1 1A17 17 0 0 1 3 4c0-.6.4-1 1-1h3.5c.6 0 1 .4 1 1 0 1.3.2 2.5.6 3.6.1.3 0 .7-.2 1z"/></svg>
    74135 | (918) 555-0147
  </div>
  <div class="footer-rule abs"></div>
  <nav class="footer-nav">
    <a style="left:233px">PRODUCTS</a>
    <a style="left:346px">SERVICES</a>
    <a style="left:448px">REVIEWS</a>
    <a style="left:545px">FINANCING</a>
    <a style="left:661px">INSPIRATION</a>
    <a style="left:786px">ABOUT US</a>
    <a style="left:892px">CONTACT</a>
  </nav>
  <p class="copyright center abs">Copyright © 2026 Talven Flooring Co. | Privacy | Accessibility</p>
</footer>

</body>
</html>
```